■依頼の目的/概要
電子書籍を出版しますので、表紙デザイン作成をお願いします。

■本のタイトル
「庭師が明かす港町の小さな商店街で愛される不思議な会話のひみつ手帳」

■本のサブタイトル
~灯りのともし方ひらきます~
殺陣師とは、映画、ドラマや舞台などでのアクションシーンを振り付け演出する人のことです。

■本の内容

「アクション」と「杉浦メソッド」の二刀流メンタルトレーナーが、「職場の空気を明るくする」秘密のコミュニケーション術を初公開します。

とてもストレスの多い職場だからこそ、適度な緊張感とリラックスした「空気づくり」が必要です。
肉体的にも精神的にも厳しい現場で学んだ「厳しくも楽しい」雰囲気作りが、俳優さんたちの最高のパフォーマンスを引き出します。
異業種からのアプローチがあなたの職場の空気を変えて、もっとあなたらしい「本物の笑顔」を取り戻していきます。

※ 参考に本を添付させていただきます。

■読者ターゲット
20代~30代くらいの看護師
(職場の人間関係での悩みを持っている)

■この本を読んで
頑張ってる人に少しでも笑顔になってもらいたい。

■デザイン要望
基本的にお任せでお願いします。(あるとすれば明るい感じでしょうか)

■イラストや写真などの素材を使用される場合は、商業利用可の素材をお願いします。(購入代金は上乗せさせていただきます)

写真や画像なしでもOK、また文字のみ、またはマンガでもOKです。

■選定確約案件になります。(必ず選定します)

■選定デザインのほかに、次点と次々点の方にも報酬を設定しています。
(各2000円づつになります)

その他何かご不明な点がございましたら、お気軽にご質問下さい。
よろしくお願いいたします。
誠に申し訳ありませんが、

ー部ワークベリー様からのご依頼により、期限を2日間(8月23日まで)
延長させて頂きます。

どうぞよろしくお願いいたします。

選定のポイントですが、女性スタッフを中心にかなり審議させていただき、それでもまとまらず、友人関係などにもアンケートを取った結果、momekalu様の提案に決定させていただきました。選定の理由として、「一目で病院関係の書籍とわかる」「信頼できそう」などがあがり、写真のデザインもかなり有力だったのですが、比べると写真は少し雑誌感がでる、それに対して当選作品は教科書感があるといったところがありました。
ピンクという色も個人的に親しみやすく受け入れやすく感じました。
皆様のご協力に心より感謝いたします。

この度は貴重なお時間の中、この案件に多数ご提案いただき本当にありがとうございました。
ワークベリーズさんに初めてお願いしたのですが、このようにクオリティの高い作品が集まることにとても驚きました。どのご提案も捨てがたく、逆に
「病院このデザインでならこんな風に書いてみたい」と私の創作意欲が刺激されるような作品もありました。選定はかなり悩みましたが、皆様の作品に触れるのがとても楽しかったです。

本当にありがとうございまいた。
心より感謝申し上げます。
皆様の益々のご活躍を祈念いたします。

```html
<!DOCTYPE html>
<html lang="ja">
<head>
<meta charset="utf-8">
<title>庭師が明かす港町の小さな商店街で愛される不思議な会話のひみつ手帳</title>
<link rel="stylesheet" href="https://fonts.googleapis.com/css2?family=Noto+Sans+JP:wght@500;700;900&family=Noto+Serif+JP:wght@700;900&display=swap">
<style>
  :root {
    --paper: #ffffff;
    --ink: #1f1f1f;
    --title-red: #e5322a;
    --title-pink: #e4489a;
    --band-orange: #f7b24b;
    --figure-tone: #f4e6ee;
  }
  html, body {
    margin: 0;
    padding: 0;
    overflow: hidden;
  }
  .cover {
    position: relative;
    width: 753px;
    height: 1200px;
    background: var(--paper);
    overflow: hidden;
    font-family: "Noto Sans JP", sans-serif;
    color: var(--ink);
  }
  .vertical {
    position: absolute;
    writing-mode: vertical-rl;
    text-orientation: upright;
    margin: 0;
    line-height: 1;
    white-space: nowrap;
  }
  .title-lead {
    right: 70px;
    top: 26px;
    color: var(--title-red);
    font-weight: 900;
    font-size: 72px;
  }
  .title-lead .particle { font-size: 50px; }
  .title-setting {
    right: 232px;
    top: 28px;
    font-weight: 700;
    font-size: 26px;
    letter-spacing: 0.02em;
  }
  .title-secret {
    right: 302px;
    top: 188px;
    font-weight: 900;
    font-size: 48px;
  }
  .title-main {
    right: 382px;
    top: 164px;
    color: var(--title-pink);
    font-weight: 900;
    font-size: 62px;
  }
  .author-role {
    left: 80px;
    top: 376px;
    font-weight: 700;
    font-size: 19px;
  }
  .author-name {
    left: 120px;
    top: 552px;
    font-weight: 900;
    font-size: 38px;
    letter-spacing: 0.06em;
  }
  .figure {
    position: absolute;
    left: 378px;
    top: 540px;
    width: 262px;
    height: 290px;
    border-radius: 40% 40% 20% 20%;
    background: radial-gradient(ellipse at 50% 40%, var(--figure-tone), rgba(244,230,238,0) 72%);
  }
  .tagline-band {
    position: absolute;
    left: 0;
    top: 828px;
    width: 753px;
    height: 372px;
    background: var(--band-orange);
    display: flex;
    flex-direction: column;
    align-items: center;
    justify-content: center;
    gap: 44px;
  }
  .tagline-band p {
    margin: 0;
    font-family: "Noto Serif JP", serif;
    font-weight: 900;
    font-size: 58px;
    letter-spacing: 0.08em;
    line-height: 1;
  }
</style>
</head>
<body>
  <main class="cover">
    <h1 class="vertical title-lead">庭師<span class="particle">が</span>明かす</h1>
    <p class="vertical title-setting">港町の小さな商店街で愛される</p>
    <p class="vertical title-secret">不思議な</p>
    <p class="vertical title-main">会話のひみつ手帳</p>

    <p class="vertical author-role">現役の殺陣師・俳優</p>
    <p class="vertical author-name">杉野陽介</p>

    <div class="figure" role="img" aria-label="刀を構える看護師姿の女性のイラスト"></div>

    <section class="tagline-band">
      <p>灯りのともし方</p>
      <p>ひらきます。</p>
    </section>
  </main>
</body>
</html>
```